Letterhead to Prospective Clients

Create a letterhead (word & canva) that I will use to send letters to prospective clients and also include the Coralwood Estate Partners Logo, My Contact Details and Interchangeable "Suburb". Use the same font and colour pallete

Maris Dulworth | "Suburb" Specialist - Redlands & Surrounds
Mobile: 0417 862 095
Email: MD@CoralwoodEstatePartners.com.au

```html
<!DOCTYPE html>
<html lang="en">
<head>
<meta charset="utf-8">
<title>Coralwood Estate Partners – Letterhead</title>
<link rel="stylesheet" href="https://fonts.googleapis.com/css2?family=Montserrat:wght@400;500&family=Lato:wght@400;700&family=Dancing+Script:wght@500&display=swap">
<style>
  :root {
    --navy: #14172f;
    --ink: #111111;
    --copper: #d9a06a;
    --backdrop: #e4e4e4;
    --paper: #ffffff;
  }
  * { margin: 0; padding: 0; box-sizing: border-box; }
  html, body {
    width: 1200px; height: 1079px; overflow: hidden;
    background: var(--backdrop);
  }
  .letterhead {
    position: absolute; left: 240px; top: 30px;
    width: 721px; height: 1019px;
    background: var(--paper);
    box-shadow: 0 4px 18px rgba(0,0,0,0.18);
    color: var(--ink);
  }
  .brand-name {
    position: absolute; left: 36px; top: 72px;
    width: 232px; white-space: nowrap;
    font-family: "Montserrat", sans-serif; font-weight: 400;
    font-size: 16px; letter-spacing: 0.2px; color: var(--navy);
  }
  .office {
    position: absolute; right: 288px; top: 60px;
    font-family: "Montserrat", sans-serif; font-size: 10.5px;
    line-height: 15.5px; text-align: right; color: #222;
    white-space: nowrap;
  }
  .office .label { color: var(--copper); }
  .office svg { vertical-align: -1px; margin-left: 3px; }
  .divider {
    position: absolute; left: 454px; top: 60px;
    width: 1.5px; height: 42px; background: var(--copper);
  }
  .contact {
    position: absolute; left: 467px; top: 60px;
    font-family: "Montserrat", sans-serif; font-size: 10.5px;
    line-height: 15px; color: #222; list-style: none;
    white-space: nowrap;
  }
  .contact li { display: flex; align-items: center; gap: 5px; }
  .contact svg { flex: none; }
  .agent {
    position: absolute; left: 36px; top: 211px;
    font-family: "Montserrat", sans-serif; color: #222;
  }
  .agent-name { font-size: 18.5px; line-height: 24px; }
  .agent-role { font-size: 13px; line-height: 18px; margin-top: 1px; }
  .recipient {
    position: absolute; left: 36px; top: 319px;
    font-family: "Lato", sans-serif; font-size: 14.5px; line-height: 17px;
  }
  .salutation {
    position: absolute; left: 36px; top: 390px;
    font-family: "Lato", sans-serif; font-weight: 700; font-size: 18px;
  }
  .body-copy {
    position: absolute; left: 36px; width: 649px;
    font-family: "Lato", sans-serif; font-size: 13.9px; line-height: 15.8px;
    text-align: justify;
  }
  .closing {
    position: absolute; left: 36px; top: 721px;
    font-family: "Lato", sans-serif; font-size: 14.5px;
  }
  .signature {
    position: absolute; left: 36px; top: 817px;
    font-family: "Dancing Script", cursive; font-weight: 500; font-size: 31px;
  }
</style>
</head>
<body>
<main class="letterhead">
  <header>
    <div class="brand-name">Coralwood Estate Partners</div>
    <address class="office" style="font-style:normal">
      Shop 4/58 Tidewater Road<br>
      , Wellport QLD 4170<svg width="7" height="9" viewBox="0 0 7 9"><path d="M3.5 0.3A3 3 0 0 0 0.5 3.3C0.5 5.4 3.5 8.7 3.5 8.7S6.5 5.4 6.5 3.3A3 3 0 0 0 3.5 0.3Z" fill="var(--copper)"/><circle cx="3.5" cy="3.3" r="1.1" fill="#fff"/></svg><br>
      <span class="label">ABN:</span> 47 318 702 915
    </address>
    <div class="divider"></div>
    <ul class="contact">
      <li><svg width="7" height="10" viewBox="0 0 7 10"><rect x="0.6" y="0.6" width="5.8" height="8.8" rx="1" fill="none" stroke="var(--copper)" stroke-width="1.1"/><rect x="2.5" y="7.4" width="2" height="0.9" fill="var(--copper)"/></svg>0417 862 095</li>
      <li><svg width="8" height="6" viewBox="0 0 8 6"><rect width="8" height="6" fill="var(--copper)"/><path d="M0 0L4 3.3L8 0" fill="none" stroke="#fff" stroke-width="0.9"/></svg>MD@CoralwoodEstatePartners.com.au</li>
      <li><svg width="8" height="8" viewBox="0 0 8 8"><circle cx="4" cy="4" r="3.6" fill="var(--copper)"/><path d="M0.5 4H7.5M4 0.4C2.4 2.4 2.4 5.6 4 7.6M4 0.4C5.6 2.4 5.6 5.6 4 7.6" fill="none" stroke="#fff" stroke-width="0.6"/></svg>www.coralwoodestatepartners.com.au</li>
    </ul>
  </header>

  <section class="agent">
    <div class="agent-name">Maris Dulworth</div>
    <div class="agent-role">"Suburb" Specialist -<br>Redlands &amp; Surrounds</div>
  </section>

  <address class="recipient" style="font-style:normal">
    Northway Holdings<br>
    123 Street Name, Suite# 10<br>
    City, State, 120023
  </address>

  <h1 class="salutation">Dear Mr, Harris</h1>

  <p class="body-copy" style="top:431px">Lorem ipsum dolor sit amet, consectetur adipiscing elit, sed do eiusmod tempor incididunt ut labore et dolore magna aliqua. Ut enim ad minim veniam, quis nostrud exercitation ullamco laboris nisi ut aliquip ex ea commodo consequat. Duis aute irure dolor in reprehenderit in voluptate velit esse cillum dolore eu fugiat nulla pariatur.</p>
  <p class="body-copy" style="top:510px">Lorem ipsum dolor sit amet, consectetur adipiscing elit, sed do eiusmod tempor incididunt ut labore et dolore magna aliqua. Ut enim ad minim veniam, quis nostrud exercitation ullamco laboris nisi ut aliquip ex ea commodo consequat. Duis aute irure dolor in reprehenderit in voluptate velit esse cillum dolore eu fugiat nulla pariatur.</p>
  <p class="body-copy" style="top:591px">Lorem ipsum dolor sit amet, consectetur adipiscing elit, sed do eiusmod tempor incididunt ut labore et dolore magna aliqua. Ut enim ad minim veniam, quis nostrud exercitation ullamco laboris nisi ut aliquip ex ea commodo consequat.</p>
  <p class="body-copy" style="top:654px">Excepteur sint occaecat cupidatat non proident, sunt in culpa qui officia deserunt mollit anim id est laborum. re et dolore magnam aliquam quaerat voluptatem.</p>

  <p class="closing">Regards</p>
  <p class="signature">Daniel Harlow</p>
</main>
</body>
</html>
```